Elegant and modern body scrub for organic junkies

I need a package design for my new company based out of Austin, Texas. We are focused on cruelty free and all natural and organic products. Our deign needs to be able to have the information we require on it, while still appearing very clean and captivating. Our initial product is a clear skin body scrub, intended for people with problematic skin. Our target market is women and we want to show elegance, without appearing "high end."
Updates

Reason: I want to allot more time for certain designers to submit edits. Last minute proposals have been appealing

Target Market(s)

Women. Organic and holistic minded. Natural beauty lovers.

Industry/Entity Type

Skin Care Product

Font styles to use
Script
Other font styles liked:
• AmericanTypewriter, Beautifulflaws, courier, caviarDreams-bold

Colors
000000
ffc214
ffffff
fece3e
fbee3e

Requirements
Must have
• Must be designed in Adobe Illustrator.
• The photo titled “structure for oz and grams” -That needs to be included at the bottom of 1B. I like the horizontal and vertical bar that separate the two. I want that.
• Color Inspiration - The photo titled “vorna color inspiration” and “color combo inspiration” are the colors I want. BLACK, GOLD, WHITE. I want the label background black and the writing in white with some gold somewhere on it. My logo is going to be a golden elephant.
• The photos titled “I like how clean this looks” and “I also like how clean this looks” - I want 1B to look super clean. I don’t want a lot of information in this box. I want simple and clean. This is where the logo and brand name will go.
• Logo - A golden elephant. I want it to be gold and geometric. There can be dimension like this elephant example on the left of the 1B description. I want the trunk to be facing to the left and the trunk needs to be raised overhead and touching the animal's forehead.
• The photo titled “sideways writing and silver rim” - I want 1C to be written sideways like this. My text will be much more extensive so the font won’t be able to be so big.
Nice to have
• The photo titled “sideways writing and silver rim” - I want 1C to be written sideways like this. My text will be much more extensive so the font won’t be able to be so big. I also REALLY like how this label is rimmed in silver, but I would want gold. This is not mandatory, but I really like this.
• The photo titled “melted honey” - This is another option I really like. The gold that looks like honey dripping on the label is really cool. Not mandatory, but I really liked that. I also like the craft background on this.
• Color Inspiration - The photo titled “color inspiration” and “another color inspiration” is an option I would also like to see. Rather than black, I’d like to see what it would ALSO look like with a navy background. NAVY, GOLD, WHITE, maybe black somewhere.
Should not have
• Colorful patterns or excessive info in section 1B.

```html
<!DOCTYPE html>
<html lang="en">
<head>
<meta charset="utf-8">
<title>Clear Skin Body Butter – Jar Label</title>
<link href="https://fonts.googleapis.com/css2?family=Courgette&family=Lato:wght@400&display=swap" rel="stylesheet">
<style>
  :root {
    --backdrop: #e4e4e4;
    --label-black: #0b0b0b;
    --gold: #c9a64a;
    --gold-deep: #8c6f2a;
    --gold-light: #e6cd86;
    --ink-white: #f4f4f4;
    --rule: #6b5a2e;
  }
  html, body {
    margin: 0;
    padding: 0;
    width: 1200px;
    height: 1000px;
    overflow: hidden;
    background: var(--backdrop);
  }
  .canvas {
    position: relative;
    width: 1200px;
    height: 1000px;
  }
  .lid {
    position: absolute;
    left: 450px;
    top: 70px;
    width: 300px;
    height: 300px;
    border-radius: 50%;
    background: var(--label-black);
    display: flex;
    align-items: center;
    justify-content: center;
  }
  .lid-emblem {
    width: 170px;
    height: 110px;
    border-radius: 10px;
    background: linear-gradient(135deg, var(--gold-light), var(--gold) 50%, var(--gold-deep));
  }
  .label {
    position: absolute;
    left: 200px;
    top: 440px;
    width: 800px;
    height: 420px;
    background: var(--label-black);
    border-radius: 14px;
  }
  .brand-name {
    position: absolute;
    left: 90px;
    top: 48px;
    margin: 0;
    font-family: "Courgette", cursive;
    font-size: 64px;
    font-weight: 400;
    color: var(--gold);
    letter-spacing: 1px;
  }
  .label-emblem {
    position: absolute;
    left: 80px;
    top: 150px;
    width: 260px;
    height: 160px;
    border-radius: 10px;
    background: linear-gradient(135deg, var(--gold-light), var(--gold) 50%, var(--gold-deep));
  }
  .product-name {
    position: absolute;
    left: 470px;
    top: 130px;
    margin: 0;
    font-family: "Courgette", cursive;
    font-size: 44px;
    line-height: 1.35;
    font-weight: 400;
    color: var(--ink-white);
  }
  .net-weight {
    position: absolute;
    left: 230px;
    top: 340px;
    width: 340px;
    height: 44px;
    display: flex;
    border: 1.5px solid var(--rule);
    font-family: "Lato", sans-serif;
    font-size: 16px;
    color: var(--gold);
  }
  .net-weight span {
    flex: 1;
    display: flex;
    align-items: center;
    justify-content: center;
  }
  .net-weight span + span {
    border-left: 1.5px solid var(--rule);
  }
</style>
</head>
<body>
  <main class="canvas">
    <div class="lid">
      <div class="lid-emblem" role="img" aria-label="Gold geometric elephant illustration on the lid"></div>
    </div>

    <section class="label">
      <h1 class="brand-name">Brand Name</h1>
      <div class="label-emblem" role="img" aria-label="Gold geometric elephant illustration"></div>
      <p class="product-name">Clear Skin<br>Body Butter</p>
      <div class="net-weight">
        <span>12oz</span>
        <span>340 g</span>
      </div>
    </section>
  </main>
</body>
</html>
```